Sleek business card design for digital agency.

Brief document attached for detailed description and inspiration. Looking for a minimalist sleek, cool, modern business card design.

Industry/Entity Type

Digital

```html
<!DOCTYPE html>
<html lang="en">
<head>
<meta charset="utf-8">
<title>Quill Forge — Business Card</title>
<link rel="stylesheet" href="https://fonts.googleapis.com/css2?family=Open+Sans:wght@400;600;700&display=swap">
<style>
  :root {
    --page: #fdfdfd;
    --card: #373737;
    --card-shade: #1f1f1f;
    --mark-faint: #262626;
    --accent: #1a7bbd;
    --text: #ececec;
    --band: #2a2a2a;
    --white: #ffffff;
  }
  * { margin: 0; padding: 0; box-sizing: border-box; }
  html, body {
    width: 1200px; height: 900px; overflow: hidden;
    background: var(--page);
    font-family: "Open Sans", Arial, sans-serif;
  }
  .canvas { position: relative; width: 1200px; height: 900px; }

  .card {
    position: absolute;
    width: 424px; height: 424px;
    background: var(--card);
    border-radius: 12px;
    overflow: hidden;
  }
  .card--front { left: 168px; top: 172px; }
  .card--back { left: 608px; top: 173px; }

  .corner-art {
    position: absolute; left: 0; top: 0;
    width: 236px; height: 178px;
    background: radial-gradient(ellipse at 0% 0%, var(--card-shade) 0%, var(--card-shade) 45%, rgba(31,31,31,0.55) 70%, rgba(31,31,31,0) 100%);
    border-bottom-right-radius: 100% 100%;
  }

  .wordmark-faint {
    position: absolute; left: 40px; top: 278px;
    font-size: 62px; font-weight: 600;
    color: var(--mark-faint);
    letter-spacing: -1px;
    white-space: nowrap;
  }
  .wordmark-faint .dot {
    display: inline-block; width: 44px; height: 44px;
    background: var(--mark-faint); border-radius: 50%;
    margin-right: 18px; vertical-align: -4px;
  }

  .contact {
    position: absolute; right: 34px; top: 153px;
    text-align: right;
    color: var(--text);
    font-size: 15px; line-height: 20.7px;
  }
  .contact__name {
    color: var(--accent);
    font-size: 19px; font-weight: 700;
    line-height: 26px; margin-bottom: 0;
  }
  .contact__role { margin-bottom: 20.7px; }

  .band {
    position: absolute; left: 0; top: 700px;
    width: 1200px; height: 200px;
    background: var(--band);
  }
  .band__mark {
    position: absolute; right: 70px; top: 96px;
    color: var(--white);
    font-size: 28px; font-weight: 600;
    white-space: nowrap; letter-spacing: -0.5px;
  }
  .band__mark .dot {
    display: inline-block; width: 22px; height: 22px;
    background: var(--white); border-radius: 50%;
    margin-right: 10px; vertical-align: -3px;
  }
</style>
</head>
<body>
<main class="canvas">
  <section class="card card--front">
    <div class="corner-art" role="img" aria-label="Dark illustrated creature claws with blue outline in the corner"></div>
    <div class="wordmark-faint"><span class="dot"></span>Quill Forge</div>
  </section>

  <section class="card card--back">
    <div class="corner-art" role="img" aria-label="Dark illustrated creature claws with blue outline in the corner"></div>
    <div class="contact">
      <p class="contact__name">Daniel Hargrove</p>
      <p>Marketing Director</p>
      <p class="contact__role">Drink order: G&amp;T with cucumber</p>
      <p>Level 2, 18 Carrow St</p>
      <p>North Brayfield NSW 2100</p>
      <p>0400 555 218</p>
      <p>03 9000 4821</p>
      <p>dhargrove@quillforge.com</p>
      <p>@dhargrove81</p>
      <p>facebook.com/QuillForge</p>
    </div>
  </section>

  <footer class="band">
    <div class="band__mark"><span class="dot"></span>Quill Forge</div>
  </footer>
</main>
</body>
</html>
```